Quellmark Exteriors Needs a New Website!

We are an exteriors company specializing in vinyl siding, Morten Calloway siding, aluminum soffit/fascia, trough. We do new construction work as well as renovations. We also build detached garages.
You can view our current website at www.quellmarkbuilders.ca
I want to completely overhaul the website.
Our services are different now as we no longer do new home construction as well as we do not do the snow clearing.
I want to focus on 2 things in particular on the website:

1/ Exterior renovations

2/ Detached Garage construction.

I have included our logo in the attached files to use as well.

Some features we would like:

1/ Be able to easily attach a video from Youtube/Vimeo to highlight a product or service
2/ Quick chat or contact button that we can talk to a potential client quickly
3/ Meet the Team page that is interesting and fresh
4/ Place for us to put in helpful exterior tips/suggestions for homeowners.

Content is not important, but looking for the best design that will attract people once they click on our page and want to renovate with us.

Target Market(s)

People looking for renovations on their home, people looking to build a detached garage.

Industry/Entity Type

Residential Construction

Coding

Coded - Design and coding required

Number of Pages Required

5+ page

Font styles to use
Sans Serif

Requirements
Must have
• Fresh and exciting home page.

Simple design. Don't want it over complicated or too much information to confuse the potential client.

Easy way to contact us.

Meet the team page that instills confidence
Nice to have
• Colour of website to go off our logo. Doesn't need to be an exact match, but something that goes well with our blue and grey.

```html
<!DOCTYPE html>
<html lang="en">
<head>
<meta charset="utf-8">
<title>Quellmark Exteriors</title>
<link rel="stylesheet" href="https://fonts.googleapis.com/css2?family=Lato:wght@400;700;900&family=Varela+Round&display=swap">
<style>
:root{
  --blue:#1b7fc4;
  --blue-deep:#1166b8;
  --grey:#6b6b6d;
  --ink:#222;
  --muted:#555;
  --field-bg:#fff;
  --section-grey:#ececec;
  --footer:#3b3d55;
  --footer-text:#d7d8e2;
  --footer-line:#555870;
  --white:#fff;
}
*{box-sizing:border-box;margin:0;padding:0}
html,body{width:1200px;height:2726px;overflow:hidden}
body{position:relative;font-family:'Lato',sans-serif;background:var(--white);color:var(--ink)}
.abs{position:absolute}

/* hero */
.hero{left:0;top:0;width:1200px;height:624px;
  background:
    radial-gradient(ellipse 520px 130px at 520px 450px,rgba(226,196,120,.55) 0%,rgba(226,196,120,0) 100%),
    radial-gradient(ellipse 260px 90px at 860px 420px,rgba(214,160,90,.35) 0%,rgba(214,160,90,0) 100%),
    linear-gradient(180deg,#2c5fb4 0%,#3b74c2 22%,#4f7fae 36%,#3c4a57 52%,#4a4d48 70%,#333330 86%,#262622 100%)}
.brand{left:98px;top:28px;width:279px;height:105px;background:var(--white);display:flex;align-items:center;justify-content:center;gap:12px}
.brand-dot{width:30px;height:30px;border-radius:50%;background:var(--blue)}
.brand-name{font-weight:900;font-size:26px;color:var(--blue);letter-spacing:.5px}
.nav{left:377px;top:84px;width:529px;height:49px;background:rgba(110,110,110,.8);display:flex;align-items:center;justify-content:space-around;padding:0 18px}
.nav a{color:var(--white);font-weight:700;font-size:14px;text-decoration:none}
.quote-btn{left:906px;top:84px;width:195px;height:49px;background:var(--blue-deep);color:var(--white);font-weight:700;font-size:14px;display:flex;align-items:center;justify-content:center}
.hero-title{left:0;top:300px;width:1164px;text-align:center;color:var(--white);font-weight:900;font-size:37px;text-shadow:0 2px 6px rgba(0,0,0,.55)}
.hero-sub{left:272px;top:357px;width:620px;text-align:center;color:var(--white);font-size:19px;line-height:22px;text-shadow:0 1px 4px rgba(0,0,0,.55)}

/* services */
.section-title{width:1200px;left:0;text-align:center;font-weight:900;font-size:30px}
.services-title{top:688px;color:var(--muted);left:-8px}
.service-photo{left:147px;top:773px;width:435px;height:317px;
  background:
    radial-gradient(ellipse 90px 120px at 185px 190px,rgba(214,150,70,.6) 0%,rgba(214,150,70,0) 100%),
    linear-gradient(90deg,rgba(60,66,74,0) 0%,rgba(60,66,74,0) 68%,#35507a 80%,#2f4a6e 100%),
    linear-gradient(180deg,#55575b 0%,#6e6a64 35%,#5a5650 65%,#8d8a82 85%,#6b6760 100%)}
.service-caption{left:147px;top:1090px;width:435px;height:57px;background:var(--grey);color:var(--white);font-weight:900;font-size:23px;display:flex;align-items:center;justify-content:space-between;padding:0 48px 0 31px}
.service-card{left:620px;top:773px;width:435px;height:374px;background:var(--blue);color:var(--white);padding:47px 58px 0 36px}
.service-card h3{font-weight:900;font-size:27px;line-height:31px;margin-bottom:10px}
.service-card p{font-size:19.5px;line-height:24px}

/* team */
.team{left:0;top:1280px;width:1200px;height:545px;background:linear-gradient(180deg,#1568c0 0%,#2a79c6 50%,#1d6fc0 100%)}
.team-title{top:1338px;color:var(--white);left:6px}
.member{top:1454px;width:260px;text-align:center;color:var(--white)}
.member-photo{width:190px;height:190px;border-radius:50%;margin:0 auto 18px;
  background:
    radial-gradient(ellipse 70px 60px at 50% 88%,rgba(70,80,100,.7) 0%,rgba(70,80,100,0) 100%),
    radial-gradient(circle at 30% 30%,#c9b26a 0%,#a49548 35%,#7c7f3e 65%,#5a6432 100%)}
.member-name{font-weight:700;font-size:20px;line-height:24px}
.member-role{font-size:16px;line-height:22px}

/* quote form */
.quote{left:0;top:1825px;width:1200px;height:607px;background:linear-gradient(180deg,#efefef 0%,#e9e9e9 100%)}
.quote-title{top:1902px;color:var(--ink);left:19px}
.field{background:var(--field-bg);border:1px solid #dcdcdc;color:#777;font-size:15px;padding:0 11px;display:flex;align-items:center}
.field.select{justify-content:space-between}
.field.textarea{align-items:flex-start;padding-top:14px}
.submit{left:791px;top:2287px;width:167px;height:49px;background:var(--blue-deep);color:var(--white);font-weight:900;font-size:13px;display:flex;align-items:center;justify-content:center;gap:8px}

/* footer */
.footer{left:0;top:2432px;width:1200px;height:294px;background:var(--footer);color:var(--footer-text);font-family:'Varela Round',sans-serif}
.footer h4{position:absolute;top:42px;font-weight:400;font-size:20px;color:var(--white)}
.contact-line{position:absolute;left:129px;font-size:13px;display:flex;align-items:center;gap:12px}
.socials{position:absolute;left:132px;top:180px;display:flex;gap:6px}
.socials span{width:26px;height:26px;border:1px solid var(--footer-text);border-radius:50%;display:flex;align-items:center;justify-content:center}
.socials span::after{content:"";width:8px;height:8px;border-radius:50%;background:var(--footer-text)}
.nav-links{position:absolute;left:396px;top:88px;font-size:11px;line-height:27.5px}
.hours{position:absolute;left:604px;top:82px;width:203px;font-size:11px}
.hours div{display:flex;justify-content:space-between;padding:10px 0 9px;border-bottom:1px solid var(--footer-line)}
.hours div:last-child{border-bottom:none}
.footer-brand{position:absolute;left:846px;top:66px;width:246px;text-align:center;font-size:32px;line-height:40px;color:#9a9cad}
.footer-rule{position:absolute;left:122px;top:240px;width:982px;height:1px;background:var(--footer-line)}
.copyright{position:absolute;left:0;top:258px;width:1258px;text-align:center;font-size:11px}
</style>
</head>
<body>

<header>
  <div class="abs hero" role="img" aria-label="Photograph of a modern two-storey house with lit garage doors at dusk"></div>
  <div class="abs brand"><span class="brand-dot"></span><span class="brand-name">QUELLMARK</span></div>
  <nav class="abs nav"><a>HOME</a><a>OUR SERVICES</a><a>MEET THE TEAM</a><a>CONTACT US</a></nav>
  <div class="abs quote-btn">REQUEST A QUOTE</div>
  <h1 class="abs hero-title">EXPERIENCE THE QUELLMARK DIFFERENCE</h1>
  <p class="abs hero-sub">Honest and reliable construction service in Edmonton and area. We take pride in each and every project.</p>
</header>

<section>
  <h2 class="abs section-title services-title">OUR SERVICES</h2>
  <div class="abs service-photo" role="img" aria-label="Photograph of a house entrance with stone and siding exterior"></div>
  <div class="abs service-caption">EXTERIOR RENOVATIONS
    <svg width="26" height="20" viewBox="0 0 26 20" fill="#fff"><rect x="0" y="0" width="4" height="3"/><rect x="7" y="0" width="19" height="3"/><rect x="0" y="6" width="4" height="3"/><rect x="7" y="6" width="14" height="3"/><rect x="0" y="12" width="4" height="3"/><rect x="7" y="12" width="10" height="3"/><rect x="0" y="17" width="4" height="3"/><rect x="7" y="17" width="6" height="3"/></svg>
  </div>
  <article class="abs service-card">
    <h3>DETACHED GARAGE CONSTRUCTION</h3>
    <p>Quellmark’s exterior division is Edmonton’s exterior finishing experts. Completing the exteriors on several hundred homes a year gives you peace of mind that the job will be done right and on budget. Specializing in both residential and commercial exteriors.</p>
  </article>
</section>

<section>
  <div class="abs team" role="img" aria-label="Blue tinted background photo of timber house framing"></div>
  <h2 class="abs section-title team-title">MEET THE TEAM</h2>
  <div class="abs member" style="left:113px"><div class="member-photo" role="img" aria-label="Portrait of the general manager"></div><div class="member-name">Darren Holloway</div><div class="member-role">General Manager</div></div>
  <div class="abs member" style="left:353px"><div class="member-photo" role="img" aria-label="Portrait of the operations manager"></div><div class="member-name">Owen Pritchard</div><div class="member-role">Operations Manager (Exteriors)</div></div>
  <div class="abs member" style="left:602px"><div class="member-photo" role="img" aria-label="Portrait of the field service manager"></div><div class="member-name">Lucas Verhoeven</div><div class="member-role">Field Service Manager</div></div>
  <div class="abs member" style="left:842px"><div class="member-photo" role="img" aria-label="Portrait of the administrative assistant"></div><div class="member-name">Marisa Delgado</div><div class="member-role">Administrative Assistant</div></div>
</section>

<section>
  <div class="abs quote" role="img" aria-label="Light grey background with faint architectural building sketch"></div>
  <h2 class="abs section-title quote-title">HOUSE REQUEST A QUOTE</h2>
  <div class="abs field" style="left:248px;top:1987px;width:337px;height:48px">Name</div>
  <div class="abs field" style="left:622px;top:1987px;width:338px;height:48px">Phone Number</div>
  <div class="abs field" style="left:248px;top:2067px;width:337px;height:48px">Email Address</div>
  <div class="abs field select" style="left:622px;top:2067px;width:338px;height:48px">Choose a Service *<span style="color:#333;font-size:11px">▼</span></div>
  <div class="abs field textarea" style="left:248px;top:2141px;width:710px;height:124px">Message</div>
  <div class="abs submit">
    <svg width="14" height="14" viewBox="0 0 14 14" fill="none" stroke="#fff" stroke-width="1.8"><path d="M7 2H2v10h10V7"/><path d="M8 1h5v5M13 1 6 8"/></svg>
    Get a quote now
  </div>
</section>

<footer class="abs footer">
  <h4 style="left:129px">Contact Us</h4>
  <div class="contact-line" style="top:92px">
    <svg width="10" height="13" viewBox="0 0 10 13" fill="#fff"><path d="M5 0a5 5 0 0 0-5 5c0 4 5 8 5 8s5-4 5-8a5 5 0 0 0-5-5zm0 7a2 2 0 1 1 0-4 2 2 0 0 1 0 4z"/></svg>48 Birchwood Rd. Hollis AB 0412</div>
  <div class="contact-line" style="top:123px">
    <svg width="12" height="12" viewBox="0 0 12 12" fill="#fff"><path d="M2.5 0 0 1.5C0 7 5 12 10.5 12L12 9.5 9 7.5 7.5 9C5.5 8 4 6.5 3 4.5L4.5 3z"/></svg>780-555-0147</div>
  <div class="contact-line" style="top:154px">
    <svg width="13" height="10" viewBox="0 0 13 10" fill="none" stroke="#fff" stroke-width="1.3"><rect x=".7" y=".7" width="11.6" height="8.6"/><path d="M.7 .7 6.5 5.5 12.3.7"/></svg>info@quellmarkbuilders.ca</div>
  <div class="socials" aria-label="Social links"><span></span><span></span><span></span><span></span><span></span></div>

  <h4 style="left:392px">Navigation</h4>
  <div class="nav-links">HOME<br>ABOUT US<br>OUR SERVICES<br>MEET THE TEAM</div>

  <h4 style="left:601px">Opening Hours</h4>
  <div class="hours">
    <div><span>Monday - Friday:</span><span>09-15h</span></div>
    <div><span>Saturday:</span><span>09-12h</span></div>
    <div><span>Sunday:</span><span>Closed</span></div>
  </div>

  <div class="footer-brand">QUELLMARK<br>EXTERIORS</div>
  <div class="footer-rule"></div>
  <div class="copyright">Copyright © 2020 Quellmark Exteriors . All Rights Reserved</div>
</footer>

</body>
</html>
```